Online Course Page

We are building a video based online course page. This project is for only the actual page that the student will watch the videos at. They will watch one vide at a time. Once one video lesson is completed then they can move to the next video lesson. The page will need to show the video player. (Main feature.) The list of lessons in the course. Instructor information. Profile picture and bio of the instructor. A Live chat button that will initiate a chat in real-time with the instructor.

The winning designer will also be asked to to design the dashboard area and other aspects of the user interface as an additional project.

Target Market(s)

Adults

Number of Pages Required

1 page

Colors
9bcb3c

Requirements
Must have
• Our logo is attached. Green and grey are our colors. Should feel modern, clean and be simple to navigate. The site will be responsive so the layout should work well on mobile devices.

```html
<!DOCTYPE html>
<html lang="en">
<head>
<meta charset="utf-8">
<title>LearnHarbor – Online Course</title>
<link href="https://fonts.googleapis.com/css2?family=Montserrat:wght@400;600;700;800&family=Open+Sans:wght@400;600;700&display=swap" rel="stylesheet">
<style>
:root{
  --green:#8dc63f;
  --green-dark:#76ad2c;
  --ink:#222;
  --text:#555;
  --muted:#888;
  --light:#f0f0f0;
  --white:#fff;
  --footer:#1f1f1f;
  --heading:'Montserrat',sans-serif;
  --body:'Open Sans',sans-serif;
}
*{box-sizing:border-box;margin:0;padding:0}
html,body{width:1200px;height:4478px;overflow:hidden}
body{font-family:var(--body);color:var(--text);background:var(--white);position:relative}
.abs{position:absolute}
.btn{display:inline-flex;align-items:center;justify-content:center;background:var(--green);color:var(--white);font-family:var(--heading);font-weight:700;font-size:12px;letter-spacing:.5px;text-transform:uppercase}
.brand{font-family:var(--heading);font-weight:700;color:var(--green);display:flex;align-items:center;gap:10px}
.brand .dot{width:30px;height:30px;border-radius:50%;background:var(--green)}
.brand span{color:var(--ink)}

/* header */
.site-header{position:absolute;top:0;left:0;width:1200px;height:104px;background:var(--white)}
.site-header .brand{left:130px;top:22px;font-size:30px}
.search{left:507px;top:22px;width:168px;height:30px;border:1px solid #ccc;font-size:10px;padding:8px 10px;color:var(--muted)}
.phone{left:743px;top:29px;font-size:11px;color:var(--ink)}
.social{display:flex;gap:12px}
.social i{width:14px;height:14px;border-radius:50%;background:#999;display:block}
.site-header .social{left:827px;top:29px}
.live-chat{height:30px;padding:0 14px;gap:6px;font-size:11px}
.site-header .live-chat{left:964px;top:20px;width:102px}
.main-nav{left:507px;top:62px;display:flex;gap:4px}
.main-nav a{font-family:var(--heading);font-size:11px;font-weight:600;color:var(--ink);padding:6px 10px;text-decoration:none;text-transform:uppercase}
.main-nav a.active{background:var(--green);color:var(--white)}

/* hero */
.hero{position:absolute;top:104px;left:0;width:1200px;height:502px;background:linear-gradient(100deg,#dfe3e6 0%,#c9cfd3 45%,#8f9aa4 70%,#4a5562 100%)}
.hero-box{left:173px;top:134px;width:382px;height:165px;background:rgba(255,255,255,.85);padding:24px 26px}
.hero-box h1{font-family:var(--heading);font-weight:800;color:var(--green);font-size:32px;line-height:1.1}
.hero-box h2{font-family:var(--heading);font-weight:600;color:var(--ink);font-size:32px;line-height:1.1}
.hero-box .btn{margin-top:14px;height:30px;padding:0 14px}
.dots{display:flex;gap:10px}
.dots i{width:8px;height:8px;border-radius:50%;background:rgba(255,255,255,.6);display:block}
.dots i.on{background:var(--green)}
.hero .dots{left:553px;top:440px}

/* gray band */
.band{position:absolute;top:606px;left:0;width:1200px;height:1051px;background:var(--light)}
.tile{position:absolute;background:linear-gradient(135deg,#4a4a4a,#1e1e1e);color:var(--white);text-align:center;display:flex;flex-direction:column;justify-content:center;align-items:center;gap:4px}
.tile h3{font-family:var(--heading);font-size:16px;font-weight:700}
.tile p{font-size:11px}
.tile .btn{margin-top:8px;height:22px;padding:0 12px;font-size:10px}
.tile.big h3{font-size:20px}
.feature{position:absolute;top:394px;width:320px;text-align:center}
.feature svg{display:block;margin:0 auto 14px}
.feature h4{font-family:var(--heading);font-size:14px;color:var(--ink);margin-bottom:10px}
.feature p{font-size:12px;line-height:1.5}
.divider{position:absolute;top:394px;width:1px;height:180px;background:#d6d6d6}
.instructor-photo{left:158px;top:663px;width:448px;height:313px;border:8px solid var(--white);box-shadow:0 4px 14px rgba(0,0,0,.15);background:linear-gradient(160deg,#f1f1f1,#cfcfcf)}
.instructor{left:678px;top:698px;width:403px}
.instructor h3{font-family:var(--heading);font-size:16px;color:var(--ink);margin-bottom:24px}
.instructor p{font-size:11.5px;line-height:1.65;text-align:justify}
.instructor .btn{margin-top:30px;height:34px;padding:0 18px}

/* video learning */
.section-title{position:absolute;left:0;width:1200px;text-align:center;font-family:var(--heading);font-weight:700;font-size:24px;color:var(--ink)}
.main-video{left:128px;top:1833px;width:938px;height:442px;border-radius:6px;background:linear-gradient(135deg,#8b99a5,#4c5762 60%,#323a42);overflow:hidden}
.main-video .play{position:absolute;left:439px;top:191px}
.main-video h3{position:absolute;left:45px;bottom:40px;font-family:var(--heading);font-weight:700;font-size:22px;line-height:1.25;color:var(--white);text-transform:uppercase}
.card{position:absolute;width:225px;height:270px;background:var(--white);box-shadow:0 1px 6px rgba(0,0,0,.15)}
.card .thumb{height:166px;position:relative}
.card .thumb svg{position:absolute;left:90px;top:60px}
.card h4{font-family:var(--body);font-size:12px;font-weight:700;color:var(--ink);padding:12px 14px 0;line-height:1.3}
.card p{font-size:10px;padding:6px 14px 0;line-height:1.4}
.card .meta{position:absolute;left:14px;right:14px;bottom:10px;display:flex;justify-content:space-between;align-items:center;font-size:11px;font-weight:600;color:var(--ink)}
.card .btn{height:20px;padding:0 10px;font-size:10px}

/* testimonials */
.testimonials{position:absolute;top:3045px;left:0;width:1200px;height:621px;background:var(--light)}
.testimonial-photo{left:164px;top:135px;width:343px;height:486px;background:linear-gradient(180deg,#e5e5e5,#5b6d86 60%,#3d4b60)}
.quote{left:615px;top:255px;width:475px;font-size:16px;line-height:1.55;color:var(--text)}
.qmark{font-family:Georgia,serif;font-size:60px;color:#bbb;line-height:1}
.author{left:618px;top:452px;font-size:12px;color:var(--ink)}
.author strong{display:block;font-family:var(--heading);font-size:12px}
.author span{font-size:10px;color:var(--text)}
.testimonials .dots{left:896px;top:558px}
.testimonials .dots i{background:#bbb}

/* cta */
.cta{position:absolute;top:3666px;left:0;width:1200px;height:442px;background:var(--green);color:var(--white);text-align:center}
.cta h2{font-family:var(--heading);font-weight:700;font-size:40px;margin-top:100px}
.cta p{width:470px;margin:16px auto 0;font-size:16px;line-height:1.55}
.cta .outline{display:inline-flex;align-items:center;justify-content:center;margin-top:34px;width:226px;height:50px;border:3px solid var(--white);font-family:var(--heading);font-weight:700;font-size:14px;letter-spacing:.5px}

/* footer */
.site-footer{position:absolute;top:4108px;left:0;width:1200px;height:370px;background:var(--footer);color:#bbb}
.site-footer .brand{left:134px;top:75px;font-size:30px}
.site-footer .brand span{color:var(--white)}
.site-footer .live-chat{left:238px;top:150px;height:28px;width:100px;font-size:10px}
.foot-col{top:74px}
.foot-col h5{font-family:var(--heading);font-size:12px;color:var(--white);margin-bottom:14px}
.foot-col li{list-style:none;font-size:11px;line-height:1.6}
.follow{left:134px;top:298px;display:flex;gap:14px;align-items:center;font-family:var(--heading);font-size:11px;font-weight:700;color:var(--white)}
.follow .social i{background:#bbb}
.copyright{left:875px;top:300px;font-size:11px}
</style>
</head>
<body>

<header class="site-header">
  <div class="abs brand"><i class="dot"></i>Learn<span>Harbor</span></div>
  <div class="abs search">SEARCH COURSES</div>
  <div class="abs phone">0123 456 789</div>
  <div class="abs social"><i></i><i></i><i></i><i></i></div>
  <a class="abs btn live-chat">
    <svg width="12" height="12" viewBox="0 0 12 12"><path d="M1 2h10v6H5l-3 3V8H1z" fill="#fff"/></svg>Live Chat</a>
  <nav class="abs main-nav">
    <a class="active">Home</a><a>About Us</a><a>Services</a><a>Courses</a><a>Videos</a><a>Testimonials</a><a>Contact Us</a>
  </nav>
</header>

<section class="hero" role="img" aria-label="Smiling man with glasses working on a laptop in a bright office">
  <div class="abs hero-box">
    <h1>LEARNING ONLINE</h1>
    <h2>video based course</h2>
    <a class="btn">Watch Now</a>
  </div>
  <div class="abs dots"><i></i><i></i><i class="on"></i><i></i><i></i></div>
</section>

<section class="band">
  <div class="tile big" style="left:113px;top:48px;width:409px;height:292px" role="img" aria-label="Laptop on a desk, software development course">
    <h3>Software Development</h3><p>Lorem Ipsum is simply dummy</p><a class="btn">Watch Now</a>
  </div>
  <div class="tile" style="left:531px;top:48px;width:275px;height:140px" role="img" aria-label="Design course">
    <h3>Design</h3><p>Lorem Ipsum is simply dummy</p></div>
  <div class="tile" style="left:815px;top:48px;width:275px;height:140px" role="img" aria-label="Business course">
    <h3>Business</h3><p>Lorem Ipsum is simply dummy</p></div>
  <div class="tile" style="left:531px;top:197px;width:275px;height:143px" role="img" aria-label="Web development course">
    <h3>Web Development</h3><p>Lorem Ipsum is simply dummy</p></div>
  <div class="tile" style="left:815px;top:197px;width:275px;height:143px" role="img" aria-label="Marketing course">
    <h3>Marketing</h3><p>Lorem Ipsum is simply dummy</p></div>

  <div class="feature" style="left:73px">
    <svg width="40" height="28" viewBox="0 0 40 28"><rect x="0" y="3" width="26" height="22" rx="3" fill="#8dc63f"/><path d="M28 10l12-7v22l-12-7z" fill="#8dc63f"/></svg>
    <h4>Unlimited Videos</h4><p>Lorem ipsum dolor sit amet, consectetur adipi<br>scing elit, sed do eiusmod tempor.</p></div>
  <div class="divider" style="left:428px"></div>
  <div class="feature" style="left:440px">
    <svg width="40" height="34" viewBox="0 0 40 34"><rect x="3" y="5" width="26" height="26" rx="3" fill="none" stroke="#8dc63f" stroke-width="3"/><path d="M14 22l3-8 16-14 5 5-16 14z" fill="#8dc63f"/></svg>
    <h4>Learn Anywhere</h4><p>Lorem ipsum dolor sit amet, consectetur adipi<br>scing elit, sed do eiusmod tempor.</p></div>
  <div class="divider" style="left:772px"></div>
  <div class="feature" style="left:786px">
    <svg width="40" height="34" viewBox="0 0 40 34"><path d="M6 20a14 14 0 0 1 28 0" fill="none" stroke="#8dc63f" stroke-width="4"/><rect x="3" y="18" width="8" height="13" rx="2" fill="#8dc63f"/><rect x="29" y="18" width="8" height="13" rx="2" fill="#8dc63f"/></svg>
    <h4>Get Support</h4><p>Lorem ipsum dolor sit amet, consectetur adipi<br>scing elit, sed do eiusmod tempor.</p></div>

  <div class="abs instructor-photo" role="img" aria-label="Portrait of the instructor, young man with glasses"></div>
  <div class="abs instructor">
    <h3>INSTRUCTOR</h3>
    <p>Sed ut perspiciatis unde omnis iste natus error sit voluptatem accusantium doloremque laudantium, totam rem aperiam, eaque ipsa quae ab illo inventore veritatis et quasi architecto beatae vitae dicta sunt explicabo. Nemo enim ipsam voluptatem quia voluptas sit aspernatur aut odit aut fugit, sed quia consequuntur magni dolores eos qui ratione voluptatem sequi nesciunt. Neque porro quisquam est, qui dolorem ipsum.</p>
    <a class="btn">Read More</a>
  </div>
</section>

<h2 class="section-title" style="top:1740px">VIDEO LEARNING</h2>
<div class="abs main-video" role="img" aria-label="Two colleagues reviewing a tablet together, featured lesson video">
  <svg class="play" width="60" height="70" viewBox="0 0 60 70"><path d="M0 0l60 35L0 70z" fill="#fff"/></svg>
  <h3>Lorem ipsum dolor sit ame<br>consectetur adipisc</h3>
</div>

<div class="card" style="left:128px;top:2293px"><div class="thumb" style="background:linear-gradient(135deg,#2c6fa8,#123a5c)" role="img" aria-label="Digital marketing lesson thumbnail"><svg width="44" height="44" viewBox="0 0 44 44"><circle cx="22" cy="22" r="22" fill="#fff" opacity=".9"/><path d="M17 13l14 9-14 9z" fill="#333"/></svg></div><h4>Lorem ipsum dolor sit ame consectetur adipisc</h4><p>At vero eos et accusamus et iusto odio dignissimos</p><div class="meta">3h 6 mins<a class="btn">Watch</a></div></div>
<div class="card" style="left:366px;top:2293px"><div class="thumb" style="background:linear-gradient(135deg,#e7e2dc,#9a8f86)" role="img" aria-label="Hands typing on a laptop lesson thumbnail"><svg width="44" height="44" viewBox="0 0 44 44"><circle cx="22" cy="22" r="22" fill="#fff" opacity=".9"/><path d="M17 13l14 9-14 9z" fill="#333"/></svg></div><h4>Lorem ipsum dolor sit ame consectetur adipisc</h4><p>At vero eos et accusamus et iusto odio dignissimos</p><div class="meta">3h 6 mins<a class="btn">Watch</a></div></div>
<div class="card" style="left:604px;top:2293px"><div class="thumb" style="background:linear-gradient(135deg,#1b8c9c,#0a2f3d)" role="img" aria-label="Stock chart lesson thumbnail"><svg width="44" height="44" viewBox="0 0 44 44"><circle cx="22" cy="22" r="22" fill="#fff" opacity=".9"/><path d="M17 13l14 9-14 9z" fill="#333"/></svg></div><h4>Lorem ipsum dolor sit ame consectetur adipisc</h4><p>At vero eos et accusamus et iusto odio dignissimos</p><div class="meta">3h 6 mins<a class="btn">Watch</a></div></div>
<div class="card" style="left:842px;top:2293px"><div class="thumb" style="background:linear-gradient(135deg,#3b4a6b,#b23a4a)" role="img" aria-label="Social media apps on a phone lesson thumbnail"><svg width="44" height="44" viewBox="0 0 44 44"><circle cx="22" cy="22" r="22" fill="#fff" opacity=".9"/><path d="M17 13l14 9-14 9z" fill="#333"/></svg></div><h4>Lorem ipsum dolor sit ame consectetur adipisc</h4><p>At vero eos et accusamus et iusto odio dignissimos</p><div class="meta">3h 6 mins<a class="btn">Watch</a></div></div>

<div class="card" style="left:128px;top:2627px"><div class="thumb" style="background:linear-gradient(135deg,#6fa4c9,#c9a36b)" role="img" aria-label="Charts and paperwork lesson thumbnail"><svg width="44" height="44" viewBox="0 0 44 44"><circle cx="22" cy="22" r="22" fill="#fff" opacity=".9"/><path d="M17 13l14 9-14 9z" fill="#333"/></svg></div><h4>Lorem ipsum dolor sit ame consectetur adipisc</h4><p>At vero eos et accusamus et iusto odio dignissimos</p><div class="meta">3h 6 mins<a class="btn">Watch</a></div></div>
<div class="card" style="left:366px;top:2627px"><div class="thumb" style="background:linear-gradient(135deg,#bfc3c6,#4b4f52)" role="img" aria-label="Tablet on a desk lesson thumbnail"><svg width="44" height="44" viewBox="0 0 44 44"><circle cx="22" cy="22" r="22" fill="#fff" opacity=".9"/><path d="M17 13l14 9-14 9z" fill="#333"/></svg></div><h4>Lorem ipsum dolor sit ame consectetur adipisc</h4><p>At vero eos et accusamus et iusto odio dignissimos</p><div class="meta">3h 6 mins<a class="btn">Watch</a></div></div>
<div class="card" style="left:604px;top:2627px"><div class="thumb" style="background:linear-gradient(135deg,#6b5a4c,#2a2420)" role="img" aria-label="Person using a phone with app icons lesson thumbnail"><svg width="44" height="44" viewBox="0 0 44 44"><circle cx="22" cy="22" r="22" fill="#fff" opacity=".9"/><path d="M17 13l14 9-14 9z" fill="#333"/></svg></div><h4>Lorem ipsum dolor sit ame consectetur adipisc</h4><p>At vero eos et accusamus et iusto odio dignissimos</p><div class="meta">3h 6 mins<a class="btn">Watch</a></div></div>
<div class="card" style="left:842px;top:2627px"><div class="thumb" style="background:linear-gradient(135deg,#1e5a3e,#0c1f2a)" role="img" aria-label="Financial data screen lesson thumbnail"><svg width="44" height="44" viewBox="0 0 44 44"><circle cx="22" cy="22" r="22" fill="#fff" opacity=".9"/><path d="M17 13l14 9-14 9z" fill="#333"/></svg></div><h4>Lorem ipsum dolor sit ame consectetur adipisc</h4><p>At vero eos et accusamus et iusto odio dignissimos</p><div class="meta">3h 6 mins<a class="btn">Watch</a></div></div>

<section class="testimonials">
  <h2 class="section-title" style="top:86px">TESTIMONIALS</h2>
  <div class="abs testimonial-photo" role="img" aria-label="Smiling woman with glasses and crossed arms"></div>
  <div class="abs qmark" style="left:566px;top:180px">“</div>
  <p class="abs quote">On the other hand, we denounce with righteous indignation and dislike men who are so beguiled and demoralized by the charms of pleasure of the moment, so blinded by desire, that they cannot foresee the pain and trouble that are bound to ensue; and equal blame through weakness of will.</p>
  <div class="abs qmark" style="left:800px;top:405px">”</div>
  <div class="abs author"><strong>MARTIN</strong><span>Leeds</span></div>
  <div class="abs dots"><i></i><i></i><i class="on"></i><i></i><i></i></div>
</section>

<section class="cta">
  <h2>LIMITED LEARNING</h2>
  <p>On the other hand, we denounce with righteous indignation and dislike men who are so beguiled and demoralized by the charms of pleasure of the moment, so blinded by desire</p>
  <a class="outline">GET STARTED NOW</a>
</section>

<footer class="site-footer">
  <div class="abs brand"><i class="dot"></i>Learn<span>Harbor</span></div>
  <a class="abs btn live-chat">
    <svg width="11" height="11" viewBox="0 0 12 12"><path d="M1 2h10v6H5l-3 3V8H1z" fill="#fff"/></svg>Live Chat</a>
  <div class="abs foot-col" style="left:445px"><h5>ABOUT US</h5><ul><li>About Us</li><li>Careers</li><li>Press Center</li><li>Become an Instructor</li></ul></div>
  <div class="abs foot-col" style="left:719px"><h5>SUPPORT</h5><ul><li>Support</li><li>Contact Us</li><li>System Requirements</li><li>Site Feedback</li></ul></div>
  <div class="abs foot-col" style="left:991px"><h5>MENU</h5><ul><li>Home</li><li>Services</li><li>Videos</li><li>Courses</li><li>Testimonials</li><li>Contact Us</li></ul></div>
  <div class="abs follow">FOLLOW US<div class="social"><i></i><i></i><i></i><i></i></div></div>
  <div class="abs copyright">Copyright © 2018 All Rights Reserved</div>
</footer>

</body>
</html>
```